New Business Card Design Project

Updated business card design. I am moving towards more coaching of, for the most part women, who are searching for more in their lives. I am an intuitive healer, homeopath and nutritionist but also an author and motivational speaker. Int the past I have included my photo on the card but that is not essential. My book is called the Brilliance of Saffron - Reclaiming the Shade of Your Spirit so my colours are typically magenta.
Target Market(s)
Women - 35 - 60 considering improving their health. However, I am also a professional speaker with a target audience including corporate and conferences.
Industry/Entity Type
Health And Wellness
Contact Information for Business Card
Delia Tranmoor, Hom, RHN, BA
www.deliatranmoor.example
delia@deliatranmoor.example
555-203-7914
Facebook, instagram and twitter logos
Look and feel
Each slider illustrates characteristics of the customer's brand and the style your logo design should communicate.

```html
<!DOCTYPE html>
<html lang="en">
<head>
<meta charset="utf-8">
<title>Delia Tranmoor — Business Card Front and Back</title>
<link rel="stylesheet" href="https://fonts.googleapis.com/css2?family=Josefin+Sans:wght@300;400&family=Roboto:wght@400&display=swap">
<style>
  :root {
    --backdrop: #1f1f1f;
    --card-paper: #f1eff2;
    --card-paper-edge: #e4e1e6;
    --ink: #231f20;
    --magenta: #d0358f;
    --purple: #7b2c8c;
    --band-start: #c93a9f;
    --band-end: #7e2c8e;
    --white: #ffffff;
    --photo-light: #7a7466;
    --photo-dark: #3c4a32;
  }
  * { box-sizing: border-box; margin: 0; padding: 0; }
  html, body { width: 1200px; height: 800px; overflow: hidden; }
  body {
    background: var(--backdrop);
    font-family: "Josefin Sans", "Helvetica Neue", sans-serif;
    position: relative;
  }
  .card {
    position: absolute;
    left: 290px;
    width: 620px;
    height: 354px;
    background: radial-gradient(ellipse at 50% 40%, var(--card-paper) 0%, var(--card-paper-edge) 100%);
    overflow: hidden;
    box-shadow: 0 12px 30px rgba(0,0,0,0.45);
  }
  .card--front { top: 26px; }
  .card--back { top: 420px; }

  .band {
    position: absolute;
    left: 0; right: 0; bottom: 0;
    background: linear-gradient(90deg, var(--band-start), var(--band-end));
  }
  .card--front .band { height: 78px; }
  .card--back .band { height: 94px; }

  .brand {
    font-family: "Josefin Sans", "Helvetica Neue", sans-serif;
    font-weight: 300;
    color: var(--ink);
    line-height: 1;
    white-space: nowrap;
  }

  .front-brand {
    position: absolute;
    top: 100px; left: 0; right: 0;
    text-align: center;
    font-size: 50px;
  }

  .tagline {
    font-family: "Josefin Sans", "Helvetica Neue", sans-serif;
    font-weight: 300;
    letter-spacing: 0.5px;
    white-space: nowrap;
  }
  .front-tagline {
    position: absolute;
    top: 190px; left: 0; right: 0;
    text-align: center;
    font-size: 26px;
    color: var(--ink);
  }
  .front-web {
    position: absolute;
    bottom: 30px; left: 0; right: 0;
    text-align: center;
    font-family: "Roboto", Arial, sans-serif;
    font-size: 13px;
    color: var(--white);
    letter-spacing: 0.5px;
  }

  .portrait-frame {
    position: absolute;
    left: 38px; top: 8px;
    width: 250px; height: 262px;
    border: 4px solid var(--purple);
    z-index: 2;
  }
  .portrait {
    width: 100%; height: 100%;
    background: linear-gradient(100deg, var(--photo-dark) 0%, #55604a 25%, #d9d6da 45%, #ecebec 60%, #a99478 80%, var(--photo-light) 100%);
  }
  .back-tagline {
    position: absolute;
    left: 40px; bottom: 24px;
    font-size: 26px;
    color: var(--white);
  }

  .socials {
    position: absolute;
    right: 26px; bottom: 22px;
    display: flex; gap: 8px;
  }
  .socials__item {
    width: 26px; height: 26px;
    border-radius: 50%;
    background: var(--white);
  }

  .identity {
    position: absolute;
    left: 318px; top: 48px;
    width: 286px;
  }
  .identity__credentials {
    font-family: "Roboto", Arial, sans-serif;
    font-size: 12px;
    color: var(--ink);
    margin-left: 44px;
    margin-bottom: 8px;
  }
  .identity .brand { font-size: 36px; }

  .contacts {
    list-style: none;
    margin-top: 44px;
    font-family: "Roboto", Arial, sans-serif;
    font-size: 13px;
    color: var(--ink);
  }
  .contacts__item {
    display: flex; align-items: center;
    gap: 8px;
    margin-bottom: 7px;
    white-space: nowrap;
  }
  .contacts__icon { width: 12px; height: 12px; flex: none; }
</style>
</head>
<body>

  <section class="card card--front" aria-label="Business card front">
    <p class="brand front-brand">Delia Tranmoor</p>
    <p class="tagline front-tagline">whole-life renewal</p>
    <div class="band">
      <p class="front-web">www.deliatranmoor.example</p>
    </div>
  </section>

  <section class="card card--back" aria-label="Business card back">
    <div class="portrait-frame">
      <div class="portrait" role="img" aria-label="Portrait photograph of Delia Tranmoor standing beside a brick wall and greenery"></div>
    </div>

    <div class="identity">
      <p class="identity__credentials">Hom, RHN, BA</p>
      <p class="brand">Delia Tranmoor</p>
      <ul class="contacts">
        <li class="contacts__item">
          <svg class="contacts__icon" viewBox="0 0 12 12" aria-hidden="true"><path d="M2 1h2.5l1 3-1.5 1a6 6 0 0 0 3 3l1-1.5 3 1V11C5 11 1 7 1 2z" fill="#d0358f"/></svg>
          <span>: 555-203-7914</span>
        </li>
        <li class="contacts__item">
          <svg class="contacts__icon" viewBox="0 0 12 12" aria-hidden="true"><rect x="1" y="2.5" width="10" height="7" fill="#d0358f"/><path d="M1 2.5l5 4 5-4" stroke="#fff" stroke-width="1" fill="none"/></svg>
          <span>: www.deliatranmoor.example</span>
        </li>
        <li class="contacts__item">
          <svg class="contacts__icon" viewBox="0 0 12 12" aria-hidden="true"><rect x="1" y="1.5" width="10" height="7" fill="none" stroke="#d0358f" stroke-width="1.4"/><rect x="4" y="9.5" width="4" height="1.5" fill="#d0358f"/></svg>
          <span>: delia@deliatranmoor.example</span>
        </li>
      </ul>
    </div>

    <div class="band">
      <p class="tagline back-tagline">whole-life renewal</p>
      <div class="socials" aria-label="Social media links">
        <span class="socials__item"></span>
        <span class="socials__item"></span>
        <span class="socials__item"></span>
      </div>
    </div>
  </section>

</body>
</html>
```